Birthday Card Design

I need a birthday card designed for my son's 7th birthday party. It needs to be a colorful, inviting, maybe fun but definitely a memorable birthday card. I would like it to be different from the normal birthday card templates I see on the Internet.
Updates

As requested, I have uploaded 3 pictures of Tovik for use as a sketch etc. Preferably, pls do not use any picture as is in the card.

Target Market(s)

My son's friends are either his classmates or children of our friends. The kid would be fairly mixed nationalities - (Indian, English, American, Chinese, Japanese and Dutch and maybe some more)The party will be in a hall (about 50x40 feet) and there will be a magician, juggler, balloon sculpting, face painting kind of entertainment. Overall we expect to have about 30-40 children at the party and including adults about 100 people total.

Industry/Entity Type

Internet

Requirements
Must have
• I am planning to have a 4 side A5 layout but am open to 2 side A5 or A4 size also. It must be folded A5 or A4 definitely because of Singapore post office limitations for bulk mailing. My Son's name is Tovik. He is turning 7 in January. The party is on 15th January from 7.00 PM to 9.00 PM.

```html
<!DOCTYPE html>
<html lang="en">
<head>
<meta charset="utf-8">
<title>Tovik's 7th Birthday Invitation</title>
<link rel="stylesheet" href="https://fonts.googleapis.com/css2?family=Quicksand:wght@300;400&family=Courgette&family=Lora:ital,wght@1,400;1,600&family=Open+Sans:wght@700&display=swap">
<style>
  :root {
    --backdrop: #000000;
    --magenta: #e6157f;
    --magenta-light: #f455ac;
    --magenta-deep: #d10c70;
    --cream: #fde9cc;
    --cream-light: #fff5dd;
    --white: #ffffff;
    --kids-tone: #e9c9a8;
    --cake-tone: #c9c8ef;
    --star-red: #e3262b;
    --star-yellow: #ffe11a;
    --star-blue: #5fc4e8;
    --squiggle-blue: #8fd3ea;
    --zigzag-red: #f0485a;
  }
  html, body {
    margin: 0;
    padding: 0;
    width: 759px;
    height: 1200px;
    overflow: hidden;
    background: var(--backdrop);
  }
  .canvas {
    position: relative;
    width: 759px;
    height: 1200px;
  }
  .card {
    position: absolute;
    display: block;
  }
  .card--front { left: 91px; top: 89px; width: 560px; height: 370px; }
  .card--inside { left: 106px; top: 749px; width: 571px; height: 377px; }
  .happy-word { font-family: "Quicksand", sans-serif; font-weight: 400; fill: var(--white); }
  .photo-label { font-family: "Open Sans", sans-serif; font-weight: 700; fill: var(--magenta); }
  .party-line { font-family: "Courgette", cursive; fill: var(--magenta); }
  .party-details { font-family: "Courgette", cursive; fill: var(--magenta); }
  .welcome-line { font-family: "Courgette", cursive; fill: var(--magenta); }
  .dear-line { font-family: "Lora", serif; font-style: italic; fill: var(--white); }
</style>
</head>
<body>
<main class="canvas">

  <svg class="card card--front" viewBox="0 0 560 370" aria-label="Invitation front">
    <defs>
      <radialGradient id="pinkBurst" cx="0.4" cy="0.4" r="0.8">
        <stop offset="0" stop-color="var(--magenta-light)"/>
        <stop offset="1" stop-color="var(--magenta-deep)"/>
      </radialGradient>
    </defs>
    <rect class="front-sky" width="560" height="370" fill="url(#pinkBurst)"/>
    <path class="front-wave" d="M0 236 C140 205 240 290 390 268 C470 256 520 238 560 242 L560 370 L0 370 Z" fill="var(--cream)"/>

    <text class="happy-word" x="108" y="165" font-size="175" textLength="78" lengthAdjust="spacingAndGlyphs">H</text>
    <circle class="photo-frame" cx="235" cy="128" r="62" fill="var(--white)"/>
    <text class="photo-label" x="235" y="118" font-size="20" text-anchor="middle">Tovik's</text>
    <text class="photo-label" x="235" y="148" font-size="20" text-anchor="middle">Photo</text>
    <text class="happy-word" x="298" y="165" font-size="175" textLength="190" lengthAdjust="spacingAndGlyphs">ppy</text>

    <rect class="cake-art" x="363" y="216" width="81" height="60" rx="14" fill="var(--cake-tone)" role="img" aria-label="Illustration of a birthday cake with candles"/>
    <rect class="kids-art" x="34" y="278" width="278" height="82" rx="16" fill="var(--kids-tone)" role="img" aria-label="Illustration of children holding hands in a row"/>

    <text class="party-line" x="350" y="326" font-size="14">Happy Birthday to Tovik</text>
    <text class="party-details" x="350" y="346" font-size="9">15 January · 7.00 PM to 9.00 PM</text>
  </svg>

  <svg class="card card--inside" viewBox="0 0 571 377" aria-label="Invitation inside">
    <defs>
      <linearGradient id="creamWash" x1="0" y1="0" x2="0" y2="1">
        <stop offset="0" stop-color="var(--cream-light)"/>
        <stop offset="1" stop-color="var(--cream)"/>
      </linearGradient>
    </defs>
    <rect width="571" height="377" fill="url(#creamWash)"/>

    <text class="welcome-line" x="10" y="50" font-size="27">welcome to my party</text>

    <path class="heart" d="M292 280 C240 240 125 200 125 130 C125 92 155 74 190 74 C240 74 275 100 292 120 C309 100 344 74 394 74 C432 74 460 95 460 132 C460 200 345 240 292 280 Z" fill="var(--magenta)"/>
    <text class="dear-line" x="292" y="132" font-size="22" text-anchor="middle">To Dear</text>
    <text class="dear-line" x="292" y="185" font-size="44" text-anchor="middle">Tovik</text>

    <polygon class="star" points="56,155 60,165 71,165 62,171 66,182 56,175 46,182 50,171 41,165 52,165" fill="var(--star-red)"/>
    <polygon class="star" points="99,186 102,192 109,192 103,196 106,203 99,199 92,203 95,196 89,192 96,192" fill="var(--star-yellow)"/>
    <polygon class="star" points="460,58 464,67 474,67 466,73 469,83 460,77 451,83 454,73 446,67 456,67" fill="var(--star-blue)"/>
    <polygon class="star" points="515,112 520,124 533,124 523,132 527,145 515,137 503,145 507,132 497,124 510,124" fill="var(--star-yellow)"/>
    <rect class="squiggle-art" x="488" y="70" width="46" height="26" rx="8" fill="var(--zigzag-red)" opacity="0.35" role="img" aria-label="Red zigzag decoration"/>
    <rect class="squiggle-art" x="20" y="196" width="42" height="22" rx="8" fill="var(--squiggle-blue)" opacity="0.45" role="img" aria-label="Blue squiggle decoration"/>
    <rect class="squiggle-art" x="82" y="228" width="30" height="40" rx="8" fill="var(--squiggle-blue)" opacity="0.45" role="img" aria-label="Blue squiggle decoration"/>

    <rect class="kids-art" x="31" y="282" width="283" height="88" rx="16" fill="var(--kids-tone)" role="img" aria-label="Illustration of children holding hands in a row"/>

    <text class="party-line" x="356" y="337" font-size="14">Happy Birthday to Tovik</text>
    <text class="party-details" x="356" y="357" font-size="9">15 January · 7.00 PM to 9.00 PM</text>
  </svg>

</main>
</body>
</html>
```